Property Management Special Flyer - this month only deal

We need a flyer that's design aligns with the style of our website and regular price package attached.
We are a high quality service company that offers property management along Sydney's Northern Beaches.
This month we want to offer a deal where we are waiving Advertising Fees and a special management rate of 5% for this month (Aug) only.
Please show all the same details as on the "Tenancy and Upkeep Bundle" flyer but advertising the fact that this month only we are waiving the $350 advertising fee and a special Management fee of 5%.
I would like an A4 print ready version (with bleed if nec), an PDF version so we can email it to clients and an editable Photoshop PSD layered file so we can edit text if necessary for future use.
We would like to use the same background image as used in the price package flyer attached (background image also attached)
We want this flyer to capture attention but still look professional and clean like our website.

```html
<!DOCTYPE html>
<html lang="en">
<head>
<meta charset="utf-8">
<title>Tenancy and Upkeep Bundle – August Special</title>
<link href="https://fonts.googleapis.com/css2?family=Open+Sans:wght@400;600;700&display=swap" rel="stylesheet">
<style>
  :root {
    --teal: #2a9fa3;
    --teal-deep: #1f7f86;
    --charcoal: #35383d;
    --paper: #ffffff;
    --table-bg: #e6e7e8;
    --muted: #8a8c8f;
    --ink: #2b2d30;
    --stage: #eeeeec;
    --alert: #c0392b;
  }
  * { margin: 0; padding: 0; box-sizing: border-box; }
  html, body {
    width: 908px; height: 1200px; overflow: hidden;
    background: var(--stage);
    font-family: "Open Sans", Arial, sans-serif;
  }
  .flyer {
    position: absolute; left: 30px; top: 0;
    width: 848px; height: 1200px;
    background: var(--paper); overflow: hidden;
  }
  .hero-photo {
    position: absolute; left: 0; top: 125px; width: 825px; height: 459px;
    background: linear-gradient(180deg, #1e86c4 0%, #4aa3d6 30%, #3d4a4e 55%, #3f6b34 80%, #2f5a2a 100%);
  }
  .hero-band {
    position: absolute; left: 0; top: 499px; width: 825px; height: 85px;
    background: var(--teal-deep); opacity: .92;
    border-bottom-right-radius: 70px;
    display: flex; align-items: center; justify-content: center;
  }
  .hero-title {
    color: #fff; font-size: 33px; font-weight: 400; letter-spacing: .2px;
    white-space: nowrap;
  }
  .offer-tag {
    position: absolute; left: 23px; top: 0; width: 185px; height: 221px;
    background: var(--charcoal);
    color: #fff; font-size: 23px; font-weight: 600; line-height: 31px;
    padding: 103px 0 0 20px;
  }
  .brand {
    position: absolute; right: 23px; top: 52px;
    display: flex; align-items: center; gap: 10px; white-space: nowrap;
  }
  .brand-mark { width: 16px; height: 16px; background: var(--teal); }
  .brand-name { font-size: 24px; font-weight: 700; color: var(--charcoal); letter-spacing: -.3px; }
  .includes {
    position: absolute; left: 23px; top: 587px; width: 370px; height: 499px;
    background: var(--teal); color: #fff;
    padding: 14px 10px 0 10px;
  }
  .includes h2 { font-size: 18px; font-weight: 400; margin-bottom: 12px; }
  .includes ul { list-style: none; }
  .includes li {
    position: relative; font-size: 14.5px; line-height: 25px;
    padding-left: 20px;
  }
  .includes li::before {
    content: ""; position: absolute; left: 2px; top: 8px;
    width: 10px; height: 10px; border-radius: 50%; background: #fff;
  }
  .includes li::after {
    content: ""; position: absolute; left: 4px; top: 11px;
    width: 3px; height: 3px; border-top: 1.5px solid var(--teal); border-right: 1.5px solid var(--teal);
    transform: rotate(45deg);
  }
  .rate-head {
    position: absolute; left: 439px; top: 623px; width: 386px; height: 47px;
    background: var(--teal); color: #fff; font-size: 17px;
    display: flex; align-items: center; padding-left: 22px;
  }
  .rate-table {
    position: absolute; left: 439px; top: 684px; width: 386px; height: 259px;
    background: var(--table-bg); padding: 14px 12px 0 12px;
  }
  .rate-row {
    display: flex; align-items: center; height: 26px; margin-bottom: 7px;
    background: #fff; font-size: 10.5px; color: var(--muted); white-space: nowrap;
  }
  .rate-row .label { width: 166px; padding-left: 8px; }
  .rate-row .value { flex: 1; }
  .rate-row.lead { color: var(--ink); }
  .rate-row.lead .value { font-weight: 600; }
  .rate-row .was { text-decoration: line-through; }
  .rate-row .waived { color: var(--alert); font-weight: 700; margin-left: 8px; }
  .thumb {
    position: absolute; top: 976px; height: 110px; border-radius: 6px;
  }
  .thumb.street { left: 439px; width: 124px; background: linear-gradient(180deg, #5fa6d6, #9aa39a 55%, #3f5a3a); }
  .thumb.promenade { left: 568px; width: 124px; background: linear-gradient(180deg, #3b86c8, #a9b2b6 55%, #5c5f5c); }
  .thumb.harbour { left: 699px; width: 126px; background: linear-gradient(180deg, #1e7ec6, #2e86b8 50%, #1c5f86); }
  .contact-bar {
    position: absolute; left: 23px; top: 1112px; width: 802px; height: 68px;
    background: var(--charcoal); border-radius: 4px;
    color: #fff; font-size: 12.5px; line-height: 18px; text-align: center;
    padding-top: 7px;
  }
</style>
</head>
<body>
  <main class="flyer">
    <div class="hero-photo" role="img" aria-label="Modern two-storey home with glass balconies and lush garden under blue sky"></div>
    <div class="hero-band"><h1 class="hero-title">TENANCY AND UPKEEP BUNDLE</h1></div>

    <div class="offer-tag">SPECIAL<br>OFFER IN<br>AUGUST</div>

    <div class="brand">
      <span class="brand-mark"></span>
      <span class="brand-name">HARBOUR CREST REALTY</span>
    </div>

    <section class="includes">
      <h2>INCLUDES:</h2>
      <ul>
        <li>Securing Tenant</li>
        <li>Reference/Database Checking</li>
        <li>Lease Preparation and Signing</li>
        <li>Direct Deposit rent collection</li>
        <li>Zero arrears policy management</li>
        <li>Payment of Rates and levies</li>
        <li>Insurance management</li>
        <li>Coordination of all repairs and maintenance</li>
        <li>Regular rent reviews and renewals</li>
        <li>Detailed ingoing, ongoing and outgoing inspections with photos and videos – viewable through your personal Landlord portal</li>
        <li>Bond management – lodging and refunding</li>
        <li>Electronic monthly and EOFY statements</li>
        <li>Annual scheduled maintenance report</li>
        <li>Regulation/compliance management</li>
        <li>Tribunal Representation</li>
      </ul>
    </section>

    <div class="rate-head">Management Rate</div>
    <section class="rate-table">
      <div class="rate-row lead"><span class="label">Management Rate:</span><span class="value">5% + GST of rental income</span></div>
      <div class="rate-row"><span class="label">Letting Fee:</span><span class="value">1 weeks rent+GST 6 or 12 month lease</span></div>
      <div class="rate-row"><span class="label">Advertising:</span><span class="value"><span class="was">$350 (Inc GST)</span><span class="waived">WAIVED</span></span></div>
      <div class="rate-row"><span class="label">Professional Photography:</span><span class="value">$199 (Inc GST) 4 x Photos</span></div>
      <div class="rate-row"><span class="label">Statements:</span><span class="value">$5.00 Per month</span></div>
      <div class="rate-row"><span class="label">Lease Preparation:</span><span class="value">No Charge</span></div>
      <div class="rate-row"><span class="label">Renewal Fees:</span><span class="value">½ Weeks Rent +GST</span></div>
    </section>

    <div class="thumb street" role="img" aria-label="Modern homes along a leafy street"></div>
    <div class="thumb promenade" role="img" aria-label="Beachside promenade with people walking"></div>
    <div class="thumb harbour" role="img" aria-label="Boats moored in a blue harbour"></div>

    <footer class="contact-bar">
      Liam Carver 0400 555 118 | Nora Vale 0400 555 246<br>
      Suite 4, 12 Shoreline Parade, Seacliff NSW 2099<br>
      hello@harbourcrestrealty.com.au | www.harbourcrestrealty.com.au
    </footer>
  </main>
</body>
</html>
```